Flyer design - company flyer

We would like to inform about and advertise our services. There fore we would like to create a flyer with that information. We'll need a design to ge it done. We are looking for a design aligned with our website and logo. CAUTION - new website. current cleverdock.de is old! You can find our new website which should be represented at: beta.cleverdock.de

```html
<!DOCTYPE html>
<html lang="de">
<head>
<meta charset="utf-8">
<title>CleverDock – Firmenflyer</title>
<link href="https://fonts.googleapis.com/css2?family=Open+Sans:wght@400;600;700&family=Source+Sans+3:wght@400;600;700&display=swap" rel="stylesheet">
<style>
:root{
  --blue:#0a8fdc;
  --blue-deep:#0f5fbf;
  --blue-light:#16a9ee;
  --dark:#323337;
  --ink:#222428;
  --grey:#5b5d63;
  --paper:#f1f2f4;
  --stage:#d4d4d4;
  --white:#ffffff;
}
*{margin:0;padding:0;box-sizing:border-box}
html,body{width:881px;height:1200px;overflow:hidden;background:var(--stage)}
body{position:relative;font-family:"Source Sans 3",sans-serif;color:var(--ink)}
.spread{position:absolute;left:66px;width:729px;height:516px;background:var(--paper);overflow:hidden}
.spread--outer{top:58px}
.spread--inner{top:641px}
.abs{position:absolute}
.layer{position:absolute;left:0;top:0}
.brand{position:absolute;display:flex;align-items:center;gap:6px;font-family:"Open Sans",sans-serif;font-weight:600;font-size:21px;letter-spacing:3px}
.brand__dot{width:12px;height:12px;border-radius:50%;background:currentColor}
.brand--white{color:var(--white)}
.brand--blue{color:var(--blue-deep)}
.heading-bar{position:absolute;left:0;top:184px;width:191px;height:17px;background:var(--dark);clip-path:polygon(0 0,100% 0,94% 100%,0 100%);color:var(--white);font-family:"Open Sans",sans-serif;font-weight:600;font-size:10px;line-height:17px;padding-left:14px}
.intro{position:absolute;left:17px;top:212px;width:250px;color:var(--white);font-size:8px;line-height:14px}
.step-label{position:absolute;color:var(--white);font-size:7px;line-height:8.5px;text-align:center;width:60px;transform:translateX(-50%)}
.contact{position:absolute;left:14px;top:422px;color:var(--white);font-size:8.4px;line-height:14.6px}
.contact li{list-style:none;display:flex;gap:7px;align-items:flex-start}
.contact svg{flex:none;margin-top:3px}
.partners-title{position:absolute;left:250px;top:428px;width:60px;text-align:center;font-size:8px;font-weight:600;letter-spacing:.4px;color:var(--grey);white-space:nowrap;transform:translateX(-20%)}
.partner-badge{position:absolute;background:#c9ccd2;border-radius:2px}
.availability{position:absolute;left:384px;top:422px;width:220px}
.availability h2{font-family:"Open Sans",sans-serif;font-weight:700;font-size:13.5px;letter-spacing:1.2px;color:var(--ink)}
.availability p{font-size:7.6px;line-height:13.5px;color:var(--grey);margin-top:9px}
.availability .url{color:var(--ink);margin-top:8px}
.tagline{position:absolute;right:12px;top:29px;font-family:"Open Sans",sans-serif;font-weight:700;font-size:9.6px;letter-spacing:.5px;color:var(--ink)}
.hero-title{position:absolute;left:13px;top:97px;color:var(--white);font-family:"Open Sans",sans-serif;font-weight:600;font-size:14px;letter-spacing:1.4px}
.rule{position:absolute;height:1px;background:var(--blue)}
.hero-copy{position:absolute;left:11px;top:140px;color:var(--white);font-size:8px;line-height:13.4px}
.section-title{position:absolute;left:12px;top:260px;font-family:"Open Sans",sans-serif;font-weight:700;font-size:9px;line-height:12.5px;color:var(--ink)}
.body-copy{position:absolute;left:11px;width:160px;font-size:6.2px;line-height:9.2px;color:var(--grey);text-align:justify}
.benefits-title{position:absolute;left:11px;top:394px;font-size:7.2px;font-weight:700;color:var(--ink)}
.benefit{position:absolute;display:flex;gap:4px;align-items:center;font-size:6.6px;color:var(--grey)}
.benefit span{display:inline-block;width:6px;height:6px;border:1px solid var(--blue);border-radius:50%}
.solution-panel{position:absolute;left:201px;top:257px;width:164px;height:217px;background:linear-gradient(180deg,var(--blue-light),var(--blue-deep));color:var(--white)}
.solution-panel h3{position:absolute;left:15px;top:11px;font-family:"Open Sans",sans-serif;font-weight:600;font-size:7.6px;letter-spacing:.4px}
.solution-item{position:absolute;left:28px;width:128px}
.solution-item h4{font-size:5.4px;font-weight:700;color:var(--ink);letter-spacing:.2px}
.solution-item p{font-size:5.1px;line-height:7.2px;margin-top:2px}
.panel-icon{position:absolute;left:-13px;width:34px;height:34px;border-radius:50%;background:var(--dark);border:2px solid var(--white);display:flex;align-items:center;justify-content:center}
.services-title{position:absolute;left:365px;width:364px;top:249px;text-align:center;font-family:"Open Sans",sans-serif;font-weight:700;font-size:8px;letter-spacing:.5px;color:var(--blue-deep)}
.services-copy{position:absolute;left:378px;width:338px;top:268px;text-align:center;font-size:6.2px;line-height:9px;color:var(--grey)}
.plan{position:absolute;top:306px;width:101px;height:164px;background:var(--white);box-shadow:0 1px 4px rgba(0,0,0,.12);text-align:center}
.plan h5{margin-top:9px;font-family:"Open Sans",sans-serif;font-weight:700;font-size:6.8px;color:var(--ink)}
.plan__icon{margin:6px auto 0;display:block}
.plan__price{font-family:"Open Sans",sans-serif;font-weight:700;font-size:11.5px;color:var(--ink)}
.plan__price small{font-size:5.5px}
.plan__unit{font-size:5.3px;color:var(--blue-deep);margin-top:3px}
.plan ul{list-style:none;text-align:left;padding:7px 8px 0 9px}
.plan li{font-size:5.7px;line-height:7px;color:var(--grey);margin-bottom:6px;padding-left:7px;position:relative}
.plan li::before{content:"";position:absolute;left:0;top:1px;width:3px;height:2px;border-left:1px solid var(--blue);border-bottom:1px solid var(--blue);transform:rotate(-45deg)}
.footer-text{position:absolute;top:491px;height:23px;line-height:23px;color:var(--white);font-family:"Open Sans",sans-serif;font-weight:700;font-size:7.6px;letter-spacing:.3px;display:flex;gap:5px;align-items:center}
</style>
</head>
<body>

<!-- Outer spread: back cover and front cover -->
<section class="spread spread--outer">
  <svg class="layer" width="729" height="516" viewBox="0 0 729 516">
    <defs>
      <linearGradient id="coverBlue" x1="0" y1="0" x2="0" y2="1">
        <stop offset="0" stop-color="#0a8fdc"/><stop offset="1" stop-color="#17abef"/>
      </linearGradient>
    </defs>
    <rect x="365" width="364" height="516" fill="#f6f6f7"/>
    <polygon points="87,0 428,0 365,121 204,401 143,516 0,516 0,150" fill="url(#coverBlue)"/>
    <polygon points="534,108 729,108 729,121 528,121" fill="var(--blue-deep)"/>
    <polygon points="729,250 729,516 577,516" fill="var(--dark)"/>
    <polygon points="620,401 729,230 729,250 640,401" fill="#ffffff" opacity=".6"/>
  </svg>
  <svg class="layer" width="729" height="516" viewBox="0 0 729 516" role="img" aria-label="Foto: Geschäftsmann vor Großstadt-Skyline berührt ein leuchtendes Datennetz über einer Weltkarte">
    <defs>
      <linearGradient id="heroPhoto" x1="0" y1="0" x2="1" y2="1">
        <stop offset="0" stop-color="#7fb6d8"/><stop offset=".55" stop-color="#4b5d86"/><stop offset="1" stop-color="#a07a88"/>
      </linearGradient>
    </defs>
    <polygon points="365,121 729,121 729,401 204,401" fill="url(#heroPhoto)"/>
  </svg>

  <div class="brand brand--white" style="left:92px;top:40px"><i class="brand__dot"></i>CLEVERDOCK</div>
  <div class="brand brand--blue" style="left:442px;top:34px"><i class="brand__dot"></i>CLEVERDOCK</div>

  <div class="heading-bar">Wie werde ich Kunde?</div>
  <p class="intro">Um Kunde bei CleverDock zu werden sind die nachfolgenden vier Schritte erforderlich.</p>

  <svg class="layer" width="260" height="360" viewBox="0 0 260 360">
    <g stroke="#ffffff" stroke-width="1" stroke-dasharray="1.5 2" fill="none">
      <line x1="50" y1="290" x2="76" y2="308"/><line x1="108" y1="308" x2="133" y2="290"/><line x1="165" y1="290" x2="190" y2="308"/>
    </g>
    <g fill="none" stroke="#ffffff" stroke-width="3">
      <circle cx="34" cy="274" r="20"/><circle cx="92" cy="318" r="20"/><circle cx="149" cy="274" r="20"/><circle cx="206" cy="318" r="20"/>
    </g>
    <g fill="none" stroke="#ffffff" stroke-width="1.3">
      <rect x="27" y="266" width="14" height="16" rx="1.5"/><path d="M30 271h8M30 275h8M30 279h5"/>
      <rect x="142" y="267" width="12" height="14" rx="1"/><path d="M146 280l12-12"/>
      <rect x="197" y="311" width="18" height="12" rx="1"/><path d="M203 327h6M206 323v4"/>
    </g>
    <path d="M84 321l16-9-6 14-3-5z" fill="#ffffff"/>
  </svg>
  <span class="step-label" style="left:34px;top:307px">Service<br>auswählen</span>
  <span class="step-label" style="left:92px;top:268px">Anfrage<br>absenden</span>
  <span class="step-label" style="left:149px;top:307px">Vertrag<br>unterschreiben</span>
  <span class="step-label" style="left:206px;top:277px">Losarbeiten</span>

  <ul class="contact">
    <li><svg width="8" height="8" viewBox="0 0 8 8"><rect width="8" height="8" rx="1" fill="#1b1c20"/><path d="M2 2l1 0 .5 1.3-.6.5a4 4 0 0 0 1.3 1.3l.5-.6L6 5v1A4 4 0 0 1 2 2z" fill="#fff"/></svg>+49 30 5550 1234</li>
    <li><svg width="8" height="8" viewBox="0 0 8 8"><rect width="8" height="8" rx="1" fill="#1b1c20"/><path d="M1.8 2.6h4.4v2.8H1.8zM1.8 2.6L4 4.2 6.2 2.6" fill="none" stroke="#fff" stroke-width=".6"/></svg>kunde@cleverdock.de</li>
    <li><svg width="8" height="8" viewBox="0 0 8 8"><rect width="8" height="8" rx="1" fill="#1b1c20"/><circle cx="4" cy="4" r="2.2" fill="none" stroke="#fff" stroke-width=".6"/><path d="M1.8 4h4.4M4 1.8v4.4" stroke="#fff" stroke-width=".5"/></svg>beta.cleverdock.de</li>
    <li><svg width="8" height="8" viewBox="0 0 8 8"><rect width="8" height="8" rx="1" fill="#1b1c20"/><path d="M4 6.5L2.3 4A1.8 1.8 0 1 1 5.7 4z" fill="#fff"/></svg><span>CleverDock UG<br>(haftungsbeschränkt)<br>Lindenweg 12, 10115 Berlin</span></li>
  </ul>

  <div class="partners-title">UNSERE PARTNER</div>
  <span class="partner-badge" style="left:228px;top:454px;width:46px;height:14px"></span>
  <span class="partner-badge" style="left:300px;top:452px;width:16px;height:16px;border-radius:50%"></span>
  <span class="partner-badge" style="left:216px;top:481px;width:72px;height:12px"></span>
  <span class="partner-badge" style="left:303px;top:478px;width:36px;height:16px;border-radius:8px"></span>

  <div class="availability">
    <h2>HOHE VERFUGBARKEIT</h2>
    <p>Wir bieten zentrale EDV-Leistungen aus hochsicheren deutschen Rechenzentren.</p>
    <p class="url">beta.cleverdock.de</p>
  </div>
</section>

<!-- Inner spread -->
<section class="spread spread--inner">
  <svg class="layer" width="729" height="516" viewBox="0 0 729 516">
    <rect x="365" width="364" height="516" fill="#f6f6f7"/>
    <polygon points="210,48 590,48 598,61 204,61" fill="var(--blue-deep)"/>
  </svg>
  <svg class="layer" width="729" height="240" viewBox="0 0 729 240" role="img" aria-label="Foto: lächelnder Mann mit Brille arbeitet an einem Laptop">
    <defs><linearGradient id="manPhoto" x1="0" y1="0" x2="1" y2="0"><stop offset="0" stop-color="#dfe3e8"/><stop offset="1" stop-color="#9bb3cf"/></linearGradient></defs>
    <rect x="143" y="61" width="222" height="172" fill="url(#manPhoto)"/>
  </svg>
  <svg class="layer" width="729" height="240" viewBox="0 0 729 240">
    <polygon points="0,61 234,61 143,233 0,233" fill="var(--dark)"/>
    <polygon points="234,61 248,61 157,233 143,233" fill="#5d5f66" opacity=".7"/>
  </svg>
  <svg class="layer" width="729" height="250" viewBox="0 0 729 250" role="img" aria-label="Foto: zwei Frauen besprechen Unterlagen an einem Laptop in einem hellen Büro">
    <defs><linearGradient id="teamPhoto" x1="0" y1="0" x2="1" y2="1"><stop offset="0" stop-color="#f1ddc6"/><stop offset=".6" stop-color="#d9b59a"/><stop offset="1" stop-color="#b65a3c"/></linearGradient></defs>
    <rect x="365" y="61" width="364" height="174" fill="url(#teamPhoto)"/>
    <path d="M365 233Q547 248 729 231" fill="none" stroke="var(--blue-deep)" stroke-width="2"/>
  </svg>

  <div class="brand brand--blue" style="left:14px;top:16px"><i class="brand__dot"></i>CLEVERDOCK</div>
  <div class="tagline">IT, DIE EINFACH FUNKTIONIERT</div>

  <h1 class="hero-title">EINFACH ARBEITEN</h1>
  <span class="rule" style="left:11px;top:123px;width:69px"></span>
  <p class="hero-copy">Wir breten kleinen Unternehmen den<br>Arbeitsplatz der Zukunft!<br>Sicher, schnell und innovativ.<br>Arbeit sie von überall!</p>

  <h2 class="section-title">EINFACH, ZUVERLÄSSIG<br>UND GÜNSTIG</h2>
  <span class="rule" style="left:11px;top:293px;width:69px"></span>
  <p class="body-copy" style="top:305px">Große Unternehmen arbeiten schon seit Jahren so und konnten damit ihre Kosten senken und die Stabilität erhöhen. Jetzt bietet CleverDock die Lösung auch für kleinste Unternehmen an.</p>
  <p class="body-copy" style="top:350px">Wir speichern Ihre Daten dauerhaft an einem sicheren Ort. Notwendige Sicherheitsvorkehrungen werden getroffen und Sie konzentrieren sich auf Ihr tägliches Geschäft.</p>
  <div class="benefits-title">Ihr Nutzen im Überblick</div>
  <div class="benefit" style="left:13px;top:411px"><span></span>Expressentstörung</div>
  <div class="benefit" style="left:13px;top:423px"><span></span>Schnelle Programme</div>
  <div class="benefit" style="left:13px;top:434px"><span></span>Professioneller Schutz</div>
  <div class="benefit" style="left:13px;top:446px"><span></span>Datensicherung</div>
  <div class="benefit" style="left:13px;top:458px"><span></span>Nachhaltig</div>
  <div class="benefit" style="left:103px;top:411px"><span></span>Planbare Kosten</div>
  <div class="benefit" style="left:103px;top:423px"><span></span>Updates</div>
  <div class="benefit" style="left:103px;top:434px"><span></span>Hohe Sicherheit</div>
  <div class="benefit" style="left:103px;top:446px"><span></span>Gewohnte Software</div>

  <aside class="solution-panel">
    <h3>IT, DIE EINFACH FUNKTIONIERT</h3>
    <div class="solution-item" style="top:36px">
      <span class="panel-icon" style="left:-42px;top:1px"><svg width="14" height="14" viewBox="0 0 14 14"><path d="M7 2L2 8h3v4h4V8h3z" fill="none" stroke="#fff" stroke-width="1.3"/></svg></span>
      <h4>DAS PROBLEM</h4>
      <p>Die Basis der IT-Probleme, die Ihren Geschäftsalltag unnötig erschweren, ist – neben dem menschlichen Faktor – der Rechner selbst, denn dort landen Viren, werden Programme lahm und gehen Daten verloren.</p>
    </div>
    <div class="solution-item" style="top:97px">
      <span class="panel-icon" style="left:-42px;top:-2px"><svg width="14" height="14" viewBox="0 0 14 14"><circle cx="7" cy="6" r="4" fill="#fff"/><rect x="5.3" y="10" width="3.4" height="2.5" fill="#fff"/></svg></span>
      <h4>UNSERE LÖSUNG</h4>
      <p>CleverDock bietet Ihnen eine Lösung, mit der die tägliche Sicherung Ihrer Daten und die Überwachung der Funktionsbereitschaft Ihres Systems gewährleistet sind.</p>
    </div>
    <div class="solution-item" style="top:157px">
      <span class="panel-icon" style="left:-42px;top:-2px"><svg width="14" height="14" viewBox="0 0 14 14"><path d="M7 1.5l4.5 1.8v3.5c0 3-2 4.8-4.5 5.7-2.5-.9-4.5-2.7-4.5-5.7V3.3z" fill="#fff"/></svg></span>
      <h4>IHRE SICHERHEIT</h4>
      <p>Wenn Sie sich fragen, wie sicher unsere Lösung ist, dann ist die Antwort ganz einfach: sehr sicher. Wir arbeiten mit Serverwerk, einem der größten Rechenzentren Deutschlands, zusammen.</p>
    </div>
  </aside>

  <h2 class="services-title">SERVICE AUSWÄHLEN</h2>
  <p class="services-copy">Wählen Sie Ihren Service. CleverDock stellt im Modell Thin Client einen vollständigen Arbeitsplatz bereit. Es wird lediglich ein Monitor benötigt um loszuarbeiten.<br>Beide Services sind mit einem bestehende PC, Laptop oder Tablet von jedem Ort aus verschlüsselt nutzbar.</p>

  <article class="plan" style="left:386px">
    <h5>THIN CLIENT</h5>
    <svg class="plan__icon" width="20" height="22" viewBox="0 0 20 22"><circle cx="10" cy="6" r="5" fill="var(--blue-deep)"/><path d="M1 22c0-6 4-9 9-9s9 3 9 9z" fill="var(--blue-deep)"/></svg>
    <div class="plan__price"><small>ab </small>€89</div>
    <div class="plan__unit">pro Benutzer/Monat</div>
    <ul><li>Mindestlaufzeit 12 Monate</li><li>Thinclient pro Benutzer inklusive</li><li>Lizenzierung des Nordsoft Betriebssystems</li><li>Max. 8 Stunden Reaktionszeit</li></ul>
  </article>
  <article class="plan" style="left:499px">
    <h5>MOBILE THIN CLIENT</h5>
    <svg class="plan__icon" width="20" height="22" viewBox="0 0 20 22"><rect x="2" y="3" width="16" height="12" rx="1.5" fill="none" stroke="var(--blue-deep)" stroke-width="2.2"/><path d="M7 19h6M10 15v4" stroke="var(--blue-deep)" stroke-width="2"/></svg>
    <div class="plan__price"><small>ab </small>€99</div>
    <div class="plan__unit">pro Benutzer/Monat</div>
    <ul><li>Mindestlaufzeit 12 Monate</li><li>Support und Management</li><li>Lizenzierung des Nordsoft Betriebssystems</li><li>Max. 8 Stunden Reaktionszeit</li></ul>
  </article>
  <article class="plan" style="left:608px">
    <h5>BRING YOUR OWN</h5>
    <svg class="plan__icon" width="22" height="22" viewBox="0 0 22 22"><circle cx="11" cy="9" r="5" fill="var(--blue-light)"/><rect x="9" y="14" width="4" height="4" fill="var(--blue-deep)"/><path d="M11 0v2M2 9h2M18 9h2M4 3l1.5 1.5M18 3l-1.5 1.5" stroke="var(--blue-deep)" stroke-width="1.3"/></svg>
    <div class="plan__price"><small>ab </small>€75</div>
    <div class="plan__unit">pro Benutzer/Monat</div>
    <ul><li>Keine Mindestlaufzeit</li><li>Nutzung mit eigenem Endgerät</li><li>Lizenzierung des Nordsoft Betriebssystems</li><li>Max. 8 Stunden Reaktionszeit</li></ul>
  </article>

  <svg class="layer" width="729" height="516" viewBox="0 0 729 516">
    <rect x="0" y="488" width="729" height="2" fill="var(--blue-deep)"/>
    <rect x="0" y="490" width="729" height="26" fill="var(--dark)"/>
    <polygon points="222,490 513,490 531,516 240,516" fill="var(--blue-deep)"/>
  </svg>
  <div class="footer-text" style="left:12px">kunde@cleverdock.de | beta.cleverdock.de</div>
  <div class="footer-text" style="left:258px"><svg width="6" height="8" viewBox="0 0 6 8"><rect x=".5" y=".5" width="5" height="7" rx="1" fill="none" stroke="#fff"/></svg>+49 30 5550 1234</div>
  <div class="footer-text" style="left:386px"><svg width="6" height="8" viewBox="0 0 6 8"><rect x=".5" y=".5" width="5" height="7" rx="1" fill="none" stroke="#fff"/></svg>+49 30 5550 1234</div>
  <div class="footer-text" style="right:12px">kunde@cleverdock.de | beta.cleverdock.de</div>
</section>

</body>
</html>
```